High School Senior Ad for annual

My son is a senior, and we bought an Ad for the back of the annual and looking for a one page Ad that meets the below specification. We have to submit out final Ad by Monday 11/07/22.

Specifications:
- Must be a JPEG @ 300 DPI.
- Full page size is 8.667 inches wide by 11.333 inches tall, or 2600 pixels by 3400 pixels.
- Do NOT take wording to the edge. Leave at least ½ inch on all sides without wording.

What we want:
- Looking for a creative artistic use of the photo we provide
- His name Tobin Garrick should be in a very artistic script at the top
- Insert the attached bible verse and text somewhere on the Ad
- I'm attaching some examples of some that we like along with the photos that we want to use. Please look at the instruction doc to understand what we are looking for.
- If you have questions, please ask

```html
<!DOCTYPE html>
<html lang="en">
<head>
<meta charset="utf-8">
<title>Tobin Garrick — Senior Ad</title>
<link href="https://fonts.googleapis.com/css2?family=Great+Vibes&family=Poppins:wght@400;500;600&display=swap" rel="stylesheet">
<style>
  :root {
    --page-bg: #ffffff;
    --navy-deep: #171c45;
    --navy: #2b3275;
    --navy-mid: #222d5e;
    --forest: #1a3a38;
    --gold: #f39c12;
    --gold-light: #f7ac2a;
    --gold-dark: #e08600;
    --white: #ffffff;
    --photo-frame: #ffffff;
  }
  * { margin: 0; padding: 0; box-sizing: border-box; }
  html, body {
    width: 1200px; height: 2564px; overflow: hidden;
    background: var(--page-bg);
  }
  .ad-page {
    position: absolute;
    left: 48px; top: 560px;
    width: 986px; height: 1290px;
    transform: scale(1.12);
    transform-origin: top left;
    overflow: hidden;
    background: linear-gradient(180deg, var(--navy) 0%, var(--navy-mid) 45%, var(--forest) 100%);
    box-shadow: 0 20px 50px rgba(0,0,0,0.35);
    font-family: "Poppins", sans-serif;
    color: var(--white);
  }
  .library-backdrop {
    position: absolute; left: 0; top: 0; width: 377px; height: 1290px;
    background: linear-gradient(180deg, #1b2050 0%, #1c2347 50%, #1a2e38 100%);
  }
  .portrait {
    position: absolute; left: 0; top: 272px; width: 420px; height: 1018px;
    background: linear-gradient(180deg, #d9c08a 0%, #c9d3ea 14%, #2a3560 30%, #9fb1dc 50%, #2a3560 68%, #c8b190 85%, #bca682 100%);
    border-radius: 150px 180px 0 0;
    opacity: 0.9;
  }
  .first-name {
    position: absolute; left: 186px; top: 20px;
    font-family: "Great Vibes", cursive;
    font-size: 142px; line-height: 1;
    color: var(--white);
  }
  .last-name {
    position: absolute; left: 202px; top: 152px;
    font-family: "Poppins", sans-serif; font-weight: 600;
    font-size: 134px; line-height: 1; letter-spacing: 1px;
    background: linear-gradient(180deg, var(--gold-light), var(--gold-dark));
    -webkit-background-clip: text; background-clip: text;
    color: transparent;
  }
  .rule {
    position: absolute; left: 420px; width: 400px; height: 3px;
    background: linear-gradient(90deg, var(--gold) 0%, var(--gold) 60%, rgba(243,156,18,0) 100%);
  }
  .rule.top { top: 324px; }
  .rule.bottom { top: 455px; }
  .verse {
    position: absolute; left: 420px; top: 336px; width: 520px;
    font-weight: 500; font-size: 28px; line-height: 38px; text-transform: uppercase;
  }
  .verse .reference { color: var(--gold); }
  .message {
    position: absolute; left: 420px; top: 472px; width: 525px;
    font-size: 16.3px; line-height: 19px;
  }
  .message p { margin-bottom: 19px; }
  .quote { position: relative; padding-left: 24px; }
  .quote-mark { color: var(--gold); font-weight: 600; }
  .quote-mark.open { position: absolute; left: 0; top: -2px; font-size: 22px; }
  .signoff { color: var(--gold); font-weight: 500; font-size: 19px; line-height: 24px; }
  .sibling-note .signoff-small { color: var(--gold); font-weight: 500; }
  .snapshot {
    position: absolute; background: var(--photo-frame); padding: 14px;
    box-shadow: 0 8px 18px rgba(0,0,0,0.45);
  }
  .snapshot .shot { width: 100%; height: 100%; }
  .snapshot.toddler { left: 88px; top: 1003px; width: 200px; height: 200px; transform: rotate(-38deg); }
  .snapshot.toddler .shot { background: linear-gradient(150deg, #c89a3c, #7e8a3c 60%, #2f7a48); }
  .snapshot.golf { left: 290px; top: 975px; width: 240px; height: 240px; transform: rotate(15deg); }
  .snapshot.golf .shot { background: linear-gradient(180deg, #9aa79b, #4b5e3a 55%, #3a5a26); }
  .snapshot.flag-wall { left: 490px; top: 955px; width: 200px; height: 200px; transform: rotate(-8deg); }
  .snapshot.flag-wall .shot { background: linear-gradient(180deg, #b33a3a, #d8c6c0 45%, #c23b3b 70%, #3a3a40); }
  .snapshot.steps { left: 695px; top: 995px; width: 220px; height: 220px; transform: rotate(15deg); }
  .snapshot.steps .shot { background: linear-gradient(160deg, #b9896a, #8aa0c8 50%, #a89478); }
</style>
</head>
<body>
  <main class="ad-page">
    <div class="library-backdrop" role="img" aria-label="Photo of library bookshelves, darkened"></div>
    <div class="portrait" role="img" aria-label="Senior portrait of Tobin in navy blazer, blue shirt and striped tie"></div>

    <h1 class="name">
      <span class="first-name">Tobin</span>
      <span class="last-name">GARRICK</span>
    </h1>

    <div class="rule top"></div>
    <h2 class="verse">Behold, children are a gift<br>from the Lord....<br><span class="reference">Psalm 127:3</span></h2>
    <div class="rule bottom"></div>

    <section class="message">
      <p>Tobin, you are a blessing from the Lord, and we are so thankful for you. You have brought so much joy and love into our lives. It has been an honor to watch you grow into an amazing, kind, in-telligent, and hard-working young man. We have loved every minute of watching you play golf for WCA. Your strong work ethic during golf season was inspiring. We are so proud of you, and we are excited to see the wonderful plans God has for your life. We will always be here to love, support, and encourage you. We hope you never outgrow your love of travel, history, and a good book!</p>
      <p>Remember,<br>
        <span class="quote"><span class="quote-mark open">&ldquo;</span>The more that you read, the more things that you will know.<br>The more that you learn, the more places you&rsquo;ll go! <span class="quote-mark">&rdquo;</span><br>&ndash; Arlo Pennick</span><br>
        <span class="signoff">Love,<br>Mom &amp; Dad</span></p>
      <p class="sibling-note">Tobin, Congrats on graduating! I hope you enjoyed your senior year as much as I did. Good luck at Harlow State; you&rsquo;ll do great!<br><span class="signoff-small">Love, Callum</span></p>
    </section>

    <figure class="snapshot toddler"><div class="shot" role="img" aria-label="Childhood photo of Tobin holding a ball"></div></figure>
    <figure class="snapshot golf"><div class="shot" role="img" aria-label="Tobin carrying a golf bag on a course"></div></figure>
    <figure class="snapshot flag-wall"><div class="shot" role="img" aria-label="Tobin beside a painted flag mural and a car"></div></figure>
    <figure class="snapshot steps"><div class="shot" role="img" aria-label="Tobin sitting on brick steps"></div></figure>
  </main>
</body>
</html>
```